Save our Business Card - We need your help

We need a fresh look on our business cards. We like it as it is, but it's not quite getting the 'wow' effect that we desire.
We're a tech startup building a cloud based solution for retailers consisting of Point of Sale, Inventory management and CRM.
The design should communicate a sense of a company that cares about the little things, design and relationships.
You can have a look at our website www.tillnest.com to get a feel for what we're like. Please feel free to message us for any further clarification
Target Market(s)
Our Customers are retail busines owners, cafe owners, other startups etc.
Industry/Entity Type
Building
Colors
Designer to choose colors to be used in the design.
Look and feel
Each slider illustrates characteristics of the customer's brand and the style your logo design should communicate.

```html
<!DOCTYPE html>
<html lang="en">
<head>
<meta charset="utf-8">
<title>TillNest Business Card</title>
<link href="https://fonts.googleapis.com/css2?family=Open+Sans:wght@600&family=PT+Serif:wght@400;700&display=swap" rel="stylesheet">
<style>
  :root {
    --stage-grey: #d2d3d5;
    --band-light: #f1f1f2;
    --stage-orange: #f7941d;
    --card-dark: #3a3a3c;
    --card-light: #dcdcdd;
    --brand-orange: #f7941d;
    --accent-red: #f05a28;
    --ink: #231f20;
    --rule: #555;
  }
  * { margin: 0; padding: 0; box-sizing: border-box; }
  html, body { width: 1200px; height: 1002px; overflow: hidden; }
  body { position: relative; background: var(--stage-grey); font-family: "Open Sans", sans-serif; }

  .stage-top { position: absolute; left: 0; top: 0; width: 1200px; height: 437px; background: var(--stage-grey); }
  .stage-band { position: absolute; left: 0; top: 437px; width: 1200px; height: 25px; background: var(--band-light); }
  .stage-bottom { position: absolute; left: 0; top: 462px; width: 1200px; height: 540px; background: var(--stage-orange); }

  .wordmark { position: absolute; display: flex; align-items: center; gap: 10px; font-weight: 600; color: var(--brand-orange); white-space: nowrap; }
  .wordmark__square { background: var(--brand-orange); flex: none; }

  .wordmark--stage { left: 930px; top: 352px; font-size: 38px; gap: 12px; }
  .wordmark--stage .wordmark__square { width: 56px; height: 56px; }

  .card { position: absolute; width: 433px; height: 222px; top: 570px; overflow: hidden; box-shadow: 5px 6px 8px rgba(0,0,0,0.35); }
  .card--front { left: 120px; background: var(--card-dark); }
  .card--back { left: 648px; background: var(--card-light); }
  .card__art { position: absolute; left: 0; top: 0; }

  .wordmark--front { left: 176px; top: 148px; font-size: 34px; }
  .wordmark--front .wordmark__square { width: 50px; height: 50px; }

  .wordmark--back-main { left: 26px; top: 46px; }
  .wordmark--back-main .wordmark__square { width: 64px; height: 64px; }

  .card__divider { position: absolute; left: 112px; top: 52px; width: 1px; height: 80px; background: var(--rule); }

  .contact { position: absolute; left: 128px; top: 60px; list-style: none; font-family: "PT Serif", serif; font-size: 15px; color: var(--ink); line-height: 19px; }
  .contact li { display: flex; align-items: center; gap: 6px; }
  .contact svg { flex: none; }

  .wordmark--back-small { left: 312px; top: 182px; font-size: 17px; gap: 5px; }
  .wordmark--back-small .wordmark__square { width: 24px; height: 24px; }
</style>
</head>
<body>
  <div class="stage-top">
    <div class="wordmark wordmark--stage"><span class="wordmark__square"></span>TillNest</div>
  </div>
  <div class="stage-band"></div>
  <div class="stage-bottom"></div>

  <section class="card card--front" aria-label="Card front">
    <svg class="card__art" width="433" height="222" viewBox="0 0 433 222">
      <circle cx="47" cy="30" r="112" fill="var(--accent-red)"/>
      <circle cx="114" cy="85" r="64" fill="var(--brand-orange)" opacity="0.62"/>
    </svg>
    <div class="wordmark wordmark--front"><span class="wordmark__square"></span>TillNest</div>
  </section>

  <section class="card card--back" aria-label="Card back">
    <svg class="card__art" width="433" height="222" viewBox="0 0 433 222">
      <circle cx="478" cy="110" r="95" fill="var(--accent-red)"/>
    </svg>
    <div class="wordmark wordmark--back-main"><span class="wordmark__square"></span></div>
    <div class="card__divider"></div>
    <ul class="contact">
      <li>
        <svg width="8" height="12" viewBox="0 0 8 12" aria-hidden="true"><circle cx="4" cy="2" r="2" fill="var(--ink)"/><rect x="2" y="5" width="4" height="7" fill="var(--ink)"/></svg>
        Maya Corder
      </li>
      <li>
        <svg width="8" height="12" viewBox="0 0 8 12" aria-hidden="true"><rect x="0.75" y="0.75" width="6.5" height="10.5" rx="1" fill="none" stroke="var(--ink)" stroke-width="1.5"/></svg>
        (XXX)XXX-XXXX
      </li>
      <li>
        <svg width="11" height="8" viewBox="0 0 11 8" aria-hidden="true"><rect width="11" height="8" fill="var(--ink)"/><path d="M0.5 0.5 L5.5 4.5 L10.5 0.5" fill="none" stroke="var(--card-light)" stroke-width="1"/></svg>
        mcorder@tillnest.com
      </li>
    </ul>
    <div class="wordmark wordmark--back-small"><span class="wordmark__square"></span>TillNest</div>
  </section>
</body>
</html>
```